Website

Project to include our logo, (files attached - logo only to be included with the company name K&T Chemicals, Inc.). Visit the website to gather additional information. www.kandtchemicals-site.example.
Emphasis should be more on the trucking, (tanker trucks), and blending capabilities. See pictures on website.
Please incorporate the logo colors into the website design; particularly the darker blue and red.
Updates
I have updated the brief on this project. :)
I have just updated the brief.
The deadline is Sunday.
Please submit your final designs.
Thanks :)
Today is the last day to submit your designs.
Industry/Entity Type
It Company
Requirements
Must have
- Tank Truck picture/s and Rail Car pictures.
See this website for tank truck and rail picture (also shown below): http://freightlens.example/562/u-s-power-surge-respite-and-a-tally-says-vbt-ostrand-and-kellaway/

```html
<!DOCTYPE html>
<html lang="en">
<head>
<meta charset="utf-8">
<title>K&amp;T Chemicals, Inc.</title>
<link href="https://fonts.googleapis.com/css2?family=PT+Sans:ital,wght@0,400;0,700;1,400&display=swap" rel="stylesheet">
<style>
:root{
  --navy:#002a5c;
  --navy-dot:#1c3f73;
  --brand-blue:#2b3990;
  --ink:#3a3a3a;
  --muted:#6b6b6b;
  --link-blue:#2e6ab3;
  --page-grey:#f0eeef;
  --panel-grey:#f6f6f6;
  --rule:#cfcfcf;
  --white:#ffffff;
}
*{margin:0;padding:0;box-sizing:border-box}
html,body{width:1200px;height:1000px;overflow:hidden}
body{font-family:"PT Sans",sans-serif;color:var(--ink);background:var(--page-grey);position:relative}
.top-band{position:absolute;left:0;top:0;width:1200px;height:397px;background:var(--white)}
.brand{position:absolute;left:207px;top:52px;width:200px}
.brand-row{display:flex;align-items:center;gap:8px}
.brand-mark{width:38px;height:38px;border-radius:50%;border:3px solid var(--brand-blue);flex:none}
.brand-name{font-size:26px;line-height:28px;font-weight:700;color:var(--brand-blue)}
.brand-details{margin-top:8px;text-align:right;font-size:6px;line-height:9px;color:var(--muted)}
.contact-top{position:absolute;left:745px;top:72px;display:flex;gap:9px}
.phone-icon{width:22px;height:22px;border-radius:50%;background:var(--brand-blue);display:flex;align-items:center;justify-content:center;margin-top:6px}
.contact-top .label{font-size:10px;font-weight:700;color:#555;line-height:14px}
.contact-top .numbers{font-size:11px;color:#777;margin-top:4px}
.contact-top .numbers b{color:var(--brand-blue)}
.nav{position:absolute;left:206px;top:153px;width:821px;height:37px;background:var(--navy);border-radius:7px 7px 0 0;display:flex;align-items:center;padding-left:30px}
.nav a{color:var(--white);font-size:11px;text-decoration:none;text-transform:uppercase}
.nav a.current{color:#9cc3ee}
.nav .sep{color:var(--white);margin:0 22px;font-size:11px}
.hero{position:absolute;left:206px;top:190px;width:821px;height:333px;overflow:hidden;
  background:linear-gradient(180deg,#c6d3df 0%,#a9b1b6 35%,#8b8f90 70%,#6c6f6a 100%)}
.hero-truck{position:absolute;left:130px;top:70px;width:440px;height:263px;
  background:linear-gradient(90deg,#8b9196 0%,#b7bcc0 40%,#e3c222 62%,#f1d02a 80%,#6f6a4a 100%);border-radius:6px}
.hero-inset{position:absolute;left:552px;top:98px;width:220px;height:220px;border-radius:50%;
  background:linear-gradient(180deg,#c3d7ea 0%,#eef0f1 45%,#d5d7d6 100%)}
.slider{position:absolute;left:340px;top:306px;display:flex;align-items:center;gap:6px}
.slider .arrow{color:var(--white);font-size:26px;line-height:20px;margin:0 6px}
.slider .dot{width:14px;height:14px;border-radius:50%;background:var(--navy-dot);border:1px solid #0b2a55}
.slider .dot.on{background:var(--white)}
.enquiries{position:absolute;left:206px;top:523px;width:821px;height:105px;background:var(--navy);border-radius:0 0 7px 7px;color:#d7dde8}
.enquiries .title{position:absolute;left:24px;top:30px;font-size:10px;font-weight:700}
.enquiries .people{position:absolute;left:157px;top:30px;font-size:8.5px;font-weight:700;line-height:20px}
.follow{position:absolute;left:566px;top:44px;font-size:17px;color:#c8d0dc}
.follow-rule{position:absolute;left:671px;top:38px;width:1px;height:38px;background:#5a7196}
.social{position:absolute;left:688px;top:39px;font-size:9px;line-height:19px}
.social li{list-style:none;display:flex;align-items:center;gap:8px}
.social i{width:15px;height:15px;border-radius:50%;display:inline-block}
.social .s1{background:#3b5b9a}.social .s2{background:#3aa6dd}
.col{position:absolute;top:628px}
.col h2{font-size:13px;font-weight:400;color:var(--navy);text-transform:uppercase}
.col p{font-size:10px;line-height:16.5px}
.col .more{position:absolute;font-size:9.5px;font-style:italic;color:#777;text-decoration:underline}
.welcome{left:207px;width:280px}
.welcome h2{margin-top:26px}
.welcome h2 span{font-size:17px}
.welcome p{margin-top:20px}
.welcome p+p{margin-top:24px}
.welcome .brand-word{color:var(--brand-blue)}
.events{left:499px;width:251px;height:290px;background:var(--panel-grey);padding:0 24px 0 29px}
.events h2{margin-top:30px}
.event{border-bottom:1px solid var(--rule);padding-bottom:12px;margin-top:20px}
.event+.event{margin-top:12px}
.event time{font-size:8px;font-style:italic;color:var(--link-blue)}
.event p{font-size:8px;line-height:12px;margin-top:6px;color:#555}
.others{left:775px;width:252px}
.others h2{margin-top:30px}
.others p.lead{margin-top:12px;font-size:9.5px;line-height:12.5px;font-weight:700;color:#777}
.others .photo{margin-top:8px;width:252px;height:100px;border-radius:6px;background:linear-gradient(180deg,#d4e3f2 0%,#f1f2f3 50%,#b9bdc0 100%)}
.footer-rule{position:absolute;left:206px;top:925px;width:821px;height:1px;background:var(--rule)}
.footer-note{position:absolute;top:955px;width:1200px;text-align:center;font-size:8px;color:#333}
.copyright{position:absolute;top:977px;width:1200px;text-align:center;font-size:8px;color:#888}
</style>
</head>
<body>
<div class="top-band"></div>

<header class="brand">
  <div class="brand-row"><span class="brand-mark"></span><span class="brand-name">K&amp;T Chemicals, Inc.</span></div>
  <div class="brand-details">118 Harbor Row • P.O. Box 210 • Linwood, Ohio 40210<br>800.555.0142 • 770.555.0187 • Fax 770.555.0190<br>www.kandtchemicals-site.example</div>
</header>

<div class="contact-top">
  <span class="phone-icon"><svg width="11" height="11" viewBox="0 0 24 24"><path fill="#fff" d="M6.6 10.8a15 15 0 0 0 6.6 6.6l2.2-2.2c.3-.3.7-.4 1-.2 1.1.4 2.3.6 3.6.6.6 0 1 .4 1 1V20c0 .6-.4 1-1 1A17 17 0 0 1 3 4c0-.6.4-1 1-1h3.5c.6 0 1 .4 1 1 0 1.3.2 2.5.6 3.6.1.3 0 .7-.2 1z"/></svg></span>
  <div>
    <div class="label">We're here for you</div>
    <div class="numbers">Phone <b>1.100.555.0100</b> (U.S.) | International <b>+1.555.010.0111</b></div>
  </div>
</div>

<nav class="nav">
  <a class="current" href="#">Home</a><span class="sep">|</span>
  <a href="#">About Us</a><span class="sep">|</span>
  <a href="#">Products</a><span class="sep">|</span>
  <a href="#">Contact Us</a>
</nav>

<section class="hero" role="img" aria-label="Yellow tanker truck driving past large steel storage silos">
  <div class="hero-truck"></div>
  <div class="hero-inset" role="img" aria-label="White chemical storage tanks under a blue sky"></div>
  <div class="slider">
    <span class="arrow">&lt;</span>
    <span class="dot on"></span><span class="dot"></span><span class="dot"></span><span class="dot"></span>
    <span class="arrow">&gt;</span>
  </div>
</section>

<section class="enquiries">
  <div class="title">For More Enqueries:</div>
  <div class="people">
    Martin Reyes / General Manager M.Reyes@KandTChemicals-site.example<br>
    Lena Fordham / Sales Manager L.Fordham@mailhub.example<br>
    Owen Becker / Operations Manager O.Becker@KandTChemicals-site.example
  </div>
  <div class="follow">FOLLOW US</div>
  <div class="follow-rule"></div>
  <ul class="social">
    <li><i class="s1"></i>Find Us on Friendline</li>
    <li><i class="s2"></i>Tweet In Chirper</li>
  </ul>
</section>

<section class="col welcome">
  <h2><span>WELCOME</span> TO OUR COMPANY</h2>
  <p><span class="brand-word">K&amp;T</span> Services was a division of the Harlow and Brent Company and was established in 1979 with the initial intent of recovering the Phosphate value of co-product 35% Phosphoric Acid from aluminum anodizing. Trisodium Phosphate was derived from this process by a</p>
  <p>The assets of K&amp;T Services were purchased in September 1993 by Martin Reyes and incorporated thereafter as <span class="brand-word">K&amp;T</span> Chemicals, Inc.</p>
  <a class="more" href="#" style="top:229px;left:0">continue &gt;&gt;</a>
</section>

<section class="col events">
  <h2>Company Events</h2>
  <div class="event"><time>11 February 2014</time><p>Lorem ipsum dolor sit amet, consectetur adipisicing elit, sed do eiusmod tempor incididunt ut labore et dolore magna aliqua. Ut enim ad minim veniam</p></div>
  <div class="event"><time>11 February 2014</time><p>Lorem ipsum dolor sit amet, consectetur adipisicing elit, sed do eiusmod tempor incididunt ut labore et dolore magna aliqua. Ut enim ad minim veniam</p></div>
  <a class="more" href="#" style="top:229px;left:42px">all events &gt;&gt;</a>
</section>

<section class="col others">
  <h2>Others</h2>
  <p class="lead">Lorem ipsum dolor sit amet, consectetur adipisicing elit, sed do eiusmod tempor incididunt ut labore et dolore magna aliqua. Ut enim ad minim veniam</p>
  <div class="photo" role="img" aria-label="Row of white chemical storage tanks"></div>
  <a class="more" href="#" style="top:229px;left:0">continue &gt;&gt;</a>
</section>

<div class="footer-rule"></div>
<p class="footer-note">If you are in need of gallon or quart case products, please visit our sister company: <b>RNQChemical.example</b></p>
<p class="copyright">© 2014 K &amp; T Chemicals, INC. All rights reserved. Design By Veldris Studio</p>
</body>
</html>
```